Business Cards for Internet Security Company

Awesome designers! This is the opportunity to help design cards for a forward thinking network security company. They use threat information gathered from peer groups to make intelligent decisions on what threats are relevant and which arent. ( not that you need this to do designs, but just so you know where they are coming from. ) :-)

We'd like to see a two side design and the deliverables will be in illustrator 4. The logo is attached and the logo colors are attached in the JPG and I've attached a an eps of the logo and icon

```html
<!DOCTYPE html>
<html lang="en">
<head>
<meta charset="utf-8">
<title>Kestrelnet Business Cards</title>
<link rel="stylesheet" href="https://fonts.googleapis.com/css2?family=Cinzel:wght@400&family=Open+Sans:wght@400;600&display=swap">
<style>
  :root {
    --backdrop: #e6e7e9;
    --card: #ffffff;
    --card-shade: #f1f2f4;
    --brand-blue: #1d5a99;
    --accent-blue: #3a91e6;
    --ink: #2b2b2b;
    --icon-dark: #333333;
    --icon-letter: #bdbdbd;
  }
  * { box-sizing: border-box; margin: 0; padding: 0; }
  html, body { width: 1200px; height: 675px; overflow: hidden; }
  body {
    background: var(--backdrop);
    font-family: "Open Sans", Arial, sans-serif;
    position: relative;
  }
  .card {
    position: absolute;
    top: 183px;
    width: 540px;
    height: 309px;
    background: radial-gradient(ellipse at 40% 40%, var(--card) 0%, var(--card-shade) 100%);
    box-shadow: 0 6px 18px rgba(0,0,0,0.15);
  }
  .card--back { left: 40px; }
  .card--front { left: 620px; }

  .brand {
    position: absolute;
    display: flex;
    flex-direction: column;
    align-items: center;
  }
  .brand__dot { border-radius: 50%; background: var(--accent-blue); }
  .brand__name {
    color: var(--brand-blue);
    font-family: "Open Sans", Arial, sans-serif;
    font-weight: 600;
    line-height: 1;
  }
  .card--back .brand { left: 0; right: 0; top: 78px; }
  .card--back .brand__dot { width: 96px; height: 96px; margin-bottom: 18px; }
  .card--back .brand__name { font-size: 40px; }

  .card--front .brand { left: 60px; top: 160px; }
  .card--front .brand__dot { width: 48px; height: 48px; margin-bottom: 12px; }
  .card--front .brand__name { font-size: 42px; }

  .holder {
    position: absolute;
    left: 300px;
    top: 38px;
    font-family: "Cinzel", "Times New Roman", serif;
    color: var(--ink);
    font-size: 21px;
    line-height: 1.3;
  }
  .holder__title { padding-left: 8px; }

  .contacts {
    position: absolute;
    left: 290px;
    top: 164px;
    list-style: none;
    font-size: 11.5px;
    color: var(--ink);
    text-transform: uppercase;
  }
  .contacts li {
    display: flex;
    align-items: flex-start;
    line-height: 17px;
    margin-bottom: 4px;
  }
  .contacts__icon {
    flex: none;
    width: 13px; height: 13px;
    margin: 2px 6px 0 0;
    border-radius: 50%;
    background: var(--icon-dark);
    color: var(--icon-letter);
    font-size: 7px;
    line-height: 13px;
    text-align: center;
  }
</style>
</head>
<body>
  <section class="card card--back" aria-label="Card back">
    <div class="brand">
      <span class="brand__dot"></span>
      <span class="brand__name">Kestrelnet</span>
    </div>
  </section>

  <section class="card card--front" aria-label="Card front">
    <div class="holder">
      <p class="holder__name">Martin Calloway</p>
      <p class="holder__title">CEO</p>
    </div>

    <div class="brand">
      <span class="brand__dot"></span>
      <span class="brand__name">Kestrelnet</span>
    </div>

    <ul class="contacts">
      <li><span class="contacts__icon">A</span><span>142 Harbour Lane<br>Northgate VIC 3999</span></li>
      <li><span class="contacts__icon">P</span><span>+61 3 5550 1234</span></li>
      <li><span class="contacts__icon">F</span><span>+61 3 5550 1234</span></li>
      <li><span class="contacts__icon">E</span><span>info@kestrelnet.com</span></li>
      <li><span class="contacts__icon">W</span><span>www.kestrelnet.com</span></li>
    </ul>
  </section>
</body>
</html>
```